Design Home Screen

We’re looking for talented UI/UX designers to create an eye-popping, modern, and fun Home Screen for the Kovana app — the future of real-time earned wage access and financial empowerment.
Your mission: make the Kovana experience come alive the moment users open the app.

Design Goals

The screen should instantly communicate energy, financial control, and trust.

The “Time on the Clock” and the “Kovana Balance” must be the stars of the screen — presented in a way that feels alive, interactive, and rewarding.

Think of how to visually celebrate a user’s progress at work and their earnings — something that makes checking the app feel fun and satisfying, not transactional.

Creative Direction

Style: Sleek, fintech-modern, with motion or visual elements that feel alive (micro-animations, glowing accents, gradient depth, or movement cues).

Tone: Confident, vibrant, and optimistic — this is a financial app that feels human and inspiring.

Color palette: Black, Gold, and Green, and any other color.

Typography: Clean, readable, and balanced between playful and professional.

Must-Have Elements

Time on the Clock – creatively displayed (e.g., countdown or progress animation as the user works).

Kovana Balance – bold, fun, and maybe even interactive (reflecting growth as the user earns).

A clean navigation structure for core tabs: Home, Access Pay, Boost, History, Profile.

Engaging micro-animations, icons, or progress indicators that make the user feel “in motion.”

Room for brand personality — the “Kovana” name and logo if desired.

```html
<!DOCTYPE html>
<html lang="en">
<head>
<meta charset="utf-8">
<title>Kovana Dashboard</title>
<link rel="stylesheet" href="https://fonts.googleapis.com/css2?family=Barlow:wght@400;500;600;700&family=Rubik:wght@700;800;900&display=swap">
<style>
:root{
  --backdrop:#434343;
  --gold:#eeb40c;
  --gold-soft:#f6c53a;
  --gold-tint:#fff7de;
  --green:#0b7a55;
  --green-dark:#066646;
  --green-tint:#e6f6f0;
  --ink:#1f1f1f;
  --muted:#555;
  --badge:#3a3a3a;
  --white:#ffffff;
  --pending:#e8a317;
  --failed:#e0151b;
}
*{box-sizing:border-box;margin:0;padding:0}
html,body{width:1200px;height:3704px;overflow:hidden;background:var(--backdrop)}
.stage{position:absolute;left:0;top:0;width:556px;height:1716px;transform:scale(2.15827);transform-origin:0 0;font-family:"Barlow",sans-serif;color:var(--ink)}
.app{position:absolute;left:71px;top:70px;width:414px;height:1575px;background:linear-gradient(#fff,#fbfbfb 40%,#f7f7f7);border-radius:16px;overflow:hidden}
.hero-arc{position:absolute;left:-73px;top:-260px;width:560px;height:495px;border-radius:50%;background:radial-gradient(circle at 50% 80%,var(--gold-soft),var(--gold) 60%)}
.abs{position:absolute}
.brand{left:0;width:414px;top:18px;text-align:center;font-family:"Rubik",sans-serif;font-weight:800;font-size:44px;color:var(--white);letter-spacing:1px}
.brand-rule{left:44px;width:328px;top:79px;border-top:1px dashed rgba(255,255,255,.75)}
.screen-title{left:42px;top:95px;font-family:"Rubik",sans-serif;font-weight:800;font-size:30px;color:var(--white);text-shadow:0 2px 2px rgba(0,0,0,.18)}
.round-btn{width:34px;height:34px;border-radius:50%;border:1.5px solid var(--white);background:rgba(255,255,255,.18);display:flex;align-items:center;justify-content:center;top:95px}
.greeting{left:43px;top:158px;width:328px;height:64px;background:var(--white);border-radius:6px;box-shadow:0 2px 8px rgba(0,0,0,.08)}
.avatar{position:absolute;left:9px;top:9px;width:46px;height:46px;border-radius:4px;background:linear-gradient(135deg,#c98f6a,#8c5a3c)}
.greeting .hello{position:absolute;left:72px;top:14px;font-size:12px}
.greeting .name{position:absolute;left:72px;top:32px;font-size:15px;font-weight:500;letter-spacing:.3px}
.greeting .gear{position:absolute;right:17px;top:15px;width:34px;height:34px;border-radius:50%;background:var(--green);display:flex;align-items:center;justify-content:center}
.stat{top:280px;width:155px;height:191px;border-radius:16px;border:2px solid var(--white);text-align:center;color:var(--white);box-shadow:0 8px 18px rgba(11,122,85,.18)}
.stat-balance{left:42px;background:radial-gradient(circle at 30% 20%,#16946a,var(--green) 70%)}
.stat-clock{left:216px;background:radial-gradient(circle at 30% 20%,var(--gold-soft),var(--gold) 70%)}
.stat .badge{width:68px;height:68px;border-radius:50%;margin:20px auto 0;display:flex;align-items:center;justify-content:center}
.stat-balance .badge{background:#1ba57a}
.stat-clock .badge{background:#f8cf5a}
.stat .label{margin-top:12px;font-size:15px;font-weight:500;line-height:20px}
.stat .value{margin-top:6px;font-family:"Rubik",sans-serif;font-weight:800;font-size:24px;letter-spacing:.5px}
.chip{top:492px;width:155px;height:65px;border-radius:8px;text-align:center;font-size:14px;padding-top:11px}
.chip-period{left:42px;background:var(--green-tint);border:1px solid #3fbf95;color:var(--green)}
.chip-hours{left:216px;background:var(--gold-tint);border:1px solid var(--gold);color:#d89a00}
.chip .meta{margin-top:7px;font-size:12px;color:var(--ink);display:flex;justify-content:center;align-items:center;gap:6px}
.action{left:43px;width:328px;height:55px;background:var(--white);border-radius:6px;box-shadow:0 2px 8px rgba(0,0,0,.09);display:flex;align-items:center;justify-content:space-between;padding:0 6px 0 20px;font-size:15px;font-weight:500}
.action .ico{width:40px;height:40px;border-radius:6px;background:var(--green);display:flex;align-items:center;justify-content:center}
.action.earn{color:var(--green);font-weight:700}
.tx-band{left:0;top:909px;width:371px;height:52px;background:var(--gold);border-radius:0 10px 10px 0;display:flex;align-items:center;color:var(--white)}
.tx-band .title{margin-left:14px;font-family:"Rubik",sans-serif;font-weight:700;font-size:17px;letter-spacing:.5px}
.tx-band .see{position:absolute;left:279px;font-size:14px;font-weight:700;text-decoration:underline}
.tx{left:43px;width:328px;height:65px;border-radius:8px;background:linear-gradient(180deg,#ededed,#dcdcdc);box-shadow:0 2px 6px rgba(0,0,0,.06)}
.tx .initials{position:absolute;left:12px;top:12px;width:40px;height:40px;border-radius:7px;background:var(--badge);color:var(--white);font-family:"Rubik",sans-serif;font-weight:800;font-size:17px;display:flex;align-items:center;justify-content:center}
.tx .who{position:absolute;left:69px;top:14px;font-size:15px;font-weight:500}
.tx .date{position:absolute;left:69px;top:35px;font-size:11px;color:var(--muted)}
.tx .amt{position:absolute;right:10px;top:14px;font-family:"Rubik",sans-serif;font-weight:700;font-size:18px}
.tx .status{position:absolute;right:10px;top:38px;font-size:12px;display:flex;align-items:center;gap:4px;color:#333}
.tx .status b{font-weight:500}
.ok{color:var(--green)}.pend{color:var(--pending)}.fail{color:var(--failed)}
.tabbar{left:0;top:1505px;width:414px;height:70px;background:var(--green);border-radius:14px 14px 16px 16px;display:flex;justify-content:space-around;align-items:center;color:var(--white);padding:0 6px}
.tab{display:flex;flex-direction:column;align-items:center;gap:5px;font-size:15px;font-weight:500}
</style>
</head>
<body>
<div class="stage">
<main class="app">
  <div class="hero-arc"></div>
  <div class="abs brand">KOVANA</div>
  <div class="abs brand-rule"></div>
  <h1 class="abs screen-title">DASHBOARD</h1>
  <div class="abs round-btn" style="left:292px"><svg width="16" height="16" viewBox="0 0 16 16" fill="none" stroke="#fff" stroke-width="1.6"><path d="M2 4h12M2 8h12M2 12h12"/><circle cx="10" cy="4" r="1.6" fill="#eeb40c"/><circle cx="5" cy="8" r="1.6" fill="#eeb40c"/><circle cx="9" cy="12" r="1.6" fill="#eeb40c"/></svg></div>
  <div class="abs round-btn" style="left:337px"><svg width="16" height="16" viewBox="0 0 16 16" fill="#fff"><path d="M8 1.5a4.5 4.5 0 0 0-4.5 4.5v3.5L2 11.5h12l-1.5-2V6A4.5 4.5 0 0 0 8 1.5z"/><circle cx="8" cy="13.5" r="1.6"/></svg></div>

  <section class="abs greeting">
    <div class="avatar" role="img" aria-label="Profile photo of the user"></div>
    <div class="hello">Hello!</div>
    <div class="name">JOHN DOE</div>
    <div class="gear"><svg width="16" height="16" viewBox="0 0 16 16"><circle cx="8" cy="8" r="5.2" fill="none" stroke="#fff" stroke-width="3" stroke-dasharray="2.2 1.9"/><circle cx="8" cy="8" r="4" fill="#fff"/><circle cx="8" cy="8" r="1.6" fill="#0b7a55"/></svg></div>
  </section>

  <section class="abs stat stat-balance">
    <div class="badge"><svg width="38" height="32" viewBox="0 0 38 32" fill="#fff"><rect x="2" y="4" width="24" height="14" rx="2" transform="rotate(-10 14 11)"/><rect x="5" y="10" width="24" height="14" rx="2"/><circle cx="17" cy="17" r="3.5" fill="#1ba57a"/><ellipse cx="30" cy="22" rx="6" ry="2.2"/><ellipse cx="30" cy="26" rx="6" ry="2.2"/><ellipse cx="30" cy="30" rx="6" ry="2"/></svg></div>
    <div class="label">STASH<br>WAGE BALANCE</div>
    <div class="value">$10.00</div>
  </section>
  <section class="abs stat stat-clock">
    <div class="badge"><svg width="32" height="34" viewBox="0 0 32 34"><rect x="13" y="1" width="6" height="4" rx="1" fill="#fff"/><circle cx="16" cy="19" r="12" fill="none" stroke="#fff" stroke-width="3.5"/><path d="M16 19V11A8 8 0 0 1 24 19z" fill="#fff"/></svg></div>
    <div class="label">ON<br>THE CLOCK</div>
    <div class="value">STATUS</div>
  </section>

  <div class="abs chip chip-period">Current Pay Period:
    <div class="meta"><svg width="11" height="11" viewBox="0 0 12 12" fill="#222"><rect x="1" y="2" width="10" height="9" rx="1"/><rect x="2" y="5" width="8" height="5" fill="#e6f6f0"/><rect x="3" y="0" width="1.5" height="3"/><rect x="7.5" y="0" width="1.5" height="3"/></svg>Mar 1 - 15, 2025</div>
  </div>
  <div class="abs chip chip-hours">Work Hours:
    <div class="meta"><svg width="11" height="11" viewBox="0 0 12 12" fill="none" stroke="#222" stroke-width="1.6"><circle cx="6" cy="6" r="4.8"/><path d="M6 3.2V6h2.2"/></svg>19:00Hrs. @ $20.00/hr</div>
  </div>

  <div class="abs action" style="top:604px">Request Money<span class="ico"><svg width="24" height="24" viewBox="0 0 24 24" fill="#fff"><rect x="9" y="2" width="13" height="11" rx="1.5"/><text x="15.5" y="11" font-size="9" font-weight="700" text-anchor="middle" fill="#0b7a55" font-family="Barlow,sans-serif">$</text><path d="M2 14h7l3 2-3 2H5v3H2z"/></svg></span></div>
  <div class="abs action" style="top:674px">Loan Access<span class="ico"><svg width="24" height="24" viewBox="0 0 24 24" fill="none" stroke="#fff" stroke-width="1.8"><path d="M9 8V5a3 3 0 0 1 6 0"/><rect x="8" y="8" width="8" height="7" rx="1" fill="#fff"/><path d="M2 17h5l4 2h5l5-3"/></svg></span></div>
  <div class="abs action" style="top:744px">Update Employment<span class="ico"><svg width="24" height="24" viewBox="0 0 24 24" fill="#fff"><circle cx="9" cy="6" r="3.5"/><path d="M3 21v-4a6 6 0 0 1 10-4.5V21z"/><rect x="13" y="14" width="9" height="7" rx="1"/><rect x="15.5" y="12" width="4" height="2.5" rx=".5"/></svg></span></div>
  <div class="abs action earn" style="top:814px">Earn $7,500<span class="ico"><svg width="24" height="24" viewBox="0 0 24 24" fill="#fff"><path d="M12 9c4 0 7 4 7 8a4 4 0 0 1-4 4H9a4 4 0 0 1-4-4c0-4 3-8 7-8z"/><path d="M9 3h6l-2 5h-2z"/><rect x="2" y="15" width="9" height="6" rx="1" fill="#0b7a55" stroke="#fff" stroke-width="1.2"/></svg></span></div>

  <section class="abs tx-band">
    <svg style="margin-left:42px" width="22" height="18" viewBox="0 0 22 18" fill="none" stroke="#fff" stroke-width="2.2"><path d="M3 8V5h14M14 2l3 3-3 3M19 10v3H5M8 16l-3-3 3-3"/></svg>
    <span class="title">TRANSACTIONS</span>
    <span class="see">See All</span>
    <svg style="position:absolute;left:340px" width="18" height="16" viewBox="0 0 18 16" fill="none" stroke="#fff" stroke-width="1.8"><path d="M1 3h16M1 8h16M1 13h16"/><circle cx="12" cy="3" r="2" fill="#eeb40c"/><circle cx="6" cy="8" r="2" fill="#eeb40c"/><circle cx="11" cy="13" r="2" fill="#eeb40c"/></svg>
  </section>

  <div class="abs tx" style="top:992px"><span class="initials">JD</span><span class="who">John Doe Inc.</span><span class="date">July 12, 2025</span><span class="amt">$350.50</span><span class="status"><svg width="11" height="11" viewBox="0 0 12 12"><circle cx="6" cy="6" r="6" fill="#0b7a55"/><path d="M3.2 6.2l2 2 3.6-4" stroke="#fff" stroke-width="1.6" fill="none"/></svg><b class="ok">Sent</b> via PayLoop</span></div>
  <div class="abs tx" style="top:1076px"><span class="initials">LI</span><span class="who">Larana Inc.</span><span class="date">July 10, 2025</span><span class="amt">$280.75</span><span class="status"><svg width="11" height="11" viewBox="0 0 12 12"><circle cx="6" cy="6" r="6" fill="#0b7a55"/><path d="M3.2 6.2l2 2 3.6-4" stroke="#fff" stroke-width="1.6" fill="none"/></svg><b class="ok">Sent</b> via PayLoop</span></div>
  <div class="abs tx" style="top:1160px"><span class="initials">GW</span><span class="who">Gigworks</span><span class="date">July 25, 2025</span><span class="amt">$1300.00</span><span class="status"><svg width="13" height="12" viewBox="0 0 13 12"><path d="M6.5 0L13 12H0z" fill="#e8a317"/><rect x="5.8" y="4" width="1.4" height="4" fill="#fff"/><rect x="5.8" y="9" width="1.4" height="1.4" fill="#fff"/></svg><b class="pend">Pending</b> via PayLoop</span></div>
  <div class="abs tx" style="top:1243px"><span class="initials">BV</span><span class="who">Blossom Vale</span><span class="date">June 14, 2025</span><span class="amt">$75.00</span><span class="status"><svg width="11" height="11" viewBox="0 0 12 12"><circle cx="6" cy="6" r="6" fill="#0b7a55"/><path d="M3.2 6.2l2 2 3.6-4" stroke="#fff" stroke-width="1.6" fill="none"/></svg><b class="ok">Sent</b> via Strivo</span></div>
  <div class="abs tx" style="top:1327px"><span class="initials">NS</span><span class="who">Nestly</span><span class="date">June 12, 2025</span><span class="amt">$100.00</span><span class="status"><svg width="11" height="11" viewBox="0 0 12 12"><circle cx="6" cy="6" r="6" fill="#0b7a55"/><path d="M3.2 6.2l2 2 3.6-4" stroke="#fff" stroke-width="1.6" fill="none"/></svg><b class="ok">Sent</b> via Zenno</span></div>
  <div class="abs tx" style="top:1411px"><span class="initials">AC</span><span class="who">Avery Clinic</span><span class="date">June 18, 2025</span><span class="amt">$151.35</span><span class="status"><svg width="11" height="11" viewBox="0 0 12 12" fill="none" stroke="#e0151b" stroke-width="1.6"><circle cx="6" cy="6" r="5"/><path d="M2.5 9.5l7-7"/></svg><b class="fail">Failed</b> via PayLoop</span></div>

  <nav class="abs tabbar">
    <div class="tab"><svg width="18" height="16" viewBox="0 0 18 16" fill="#fff"><path d="M9 1l8 7h-2.5v7h-4v-4.5h-3V15h-4V8H1z"/></svg>HOME</div>
    <div class="tab"><svg width="20" height="16" viewBox="0 0 20 16" fill="none" stroke="#fff" stroke-width="1.8"><rect x="1" y="2" width="18" height="12" rx="1.5"/><path d="M1 6h18" stroke-width="2.5"/><path d="M4 11h5"/></svg>ACCESS PAY</div>
    <div class="tab"><svg width="18" height="16" viewBox="0 0 18 16" fill="#fff"><path d="M4 1h10v4a5 5 0 0 1-10 0z"/><path d="M4 2H1v2a3 3 0 0 0 3 3M14 2h3v2a3 3 0 0 1-3 3" fill="none" stroke="#fff" stroke-width="1.5"/><rect x="8" y="10" width="2" height="3"/><rect x="5" y="13" width="8" height="2.5" rx=".5"/></svg>BOOST</div>
    <div class="tab"><svg width="20" height="16" viewBox="0 0 20 16" fill="none" stroke="#fff" stroke-width="1.6"><rect x="1" y="1" width="18" height="14" rx="1.5"/><path d="M4 5h2M8 5h8M4 8h2M8 8h8M4 11h2M8 11h8"/></svg>HISTORY</div>
    <div class="tab"><svg width="16" height="16" viewBox="0 0 16 16" fill="#fff"><circle cx="8" cy="4.5" r="4"/><path d="M1 16v-2a5 5 0 0 1 5-5h4a5 5 0 0 1 5 5v2z"/></svg>PROFILE</div>
  </nav>
</main>
</div>
</body>
</html>
```